Digital Marketing Brochure - PDF

I am seeking to have a digital marketing brochure consistent with our webpage of birchwellgroup.com that includes our staff, territory and will have available links to a share file for our insurance documents and rates, etc. - I have uploaded our logo and would like you work with our webpage to keep consistent. We would like this to be a pdf style document that reads like a book and has pleasing modern, rustic appearance consistent with our web page.

Target Market(s)

Insurance companies

Industry/Entity Type

Insurance

Requirements
Must have
• Flip through marketing brochure. Essentially want it to be our webpage in a e-mailable or downloadable pdf.

```html
<!DOCTYPE html>
<html lang="en">
<head>
<meta charset="utf-8">
<title>Birchwell – When It Happens</title>
<link rel="stylesheet" href="https://fonts.googleapis.com/css2?family=Bebas+Neue&family=Montserrat:wght@800&family=Open+Sans:wght@400;600&family=Roboto:wght@700&family=Nunito:wght@400&display=swap">
<style>
  :root {
    --navy: #0a2a5e;
    --orange: #ee5325;
    --orange-deep: #c8461c;
    --ember: #e8873e;
    --smoke: #5a3420;
    --white: #ffffff;
    --stage: #eef0f3;
  }
  html, body {
    margin: 0;
    width: 1200px;
    height: 838px;
    overflow: hidden;
    background: var(--stage);
  }
  .cover-wrap {
    position: absolute;
    left: 313px;
    top: 14px;
    width: 573px;
    height: 810px;
  }
  .cover {
    position: relative;
    width: 588px;
    height: 832px;
    background: var(--navy);
    transform: scale(0.974);
    transform-origin: 0 0;
    overflow: hidden;
  }
  .cover-art {
    position: absolute;
    inset: 0;
    width: 588px;
    height: 832px;
  }
  .brand {
    position: absolute;
    right: 12px;
    top: 46px;
    text-align: right;
    color: var(--white);
  }
  .brand-name {
    font-family: "Montserrat", sans-serif;
    font-weight: 800;
    font-size: 40px;
    line-height: 1;
    letter-spacing: 1px;
  }
  .brand-sub {
    margin-top: 8px;
    font-family: "Open Sans", sans-serif;
    font-size: 10px;
    letter-spacing: 0.2px;
  }
  .headline {
    position: absolute;
    left: 42px;
    top: 600px;
    margin: 0;
    font-family: "Bebas Neue", sans-serif;
    font-weight: 400;
    font-size: 66px;
    line-height: 0.92;
    color: var(--white);
  }
  .perils {
    position: absolute;
    left: 42px;
    top: 717px;
    margin: 0;
    font-family: "Roboto", sans-serif;
    font-weight: 700;
    font-size: 17px;
    color: var(--orange);
  }
  .service-band {
    position: absolute;
    left: 3px;
    right: 0;
    top: 754px;
    height: 41px;
    background: var(--orange);
    display: flex;
    align-items: center;
    padding-left: 37px;
    font-family: "Roboto", sans-serif;
    font-weight: 700;
    font-size: 18.5px;
    color: var(--white);
  }
  .web-address {
    position: absolute;
    left: 0;
    right: 0;
    top: 805px;
    text-align: center;
    font-family: "Nunito", sans-serif;
    font-size: 14.5px;
    color: var(--white);
  }
</style>
</head>
<body>
  <div class="cover-wrap">
    <article class="cover">
      <svg class="cover-art" viewBox="0 0 588 832" aria-hidden="false">
        <defs>
          <linearGradient id="fire-tone" x1="0" y1="0" x2="1" y2="1">
            <stop offset="0" stop-color="#f3a15e"/>
            <stop offset="0.45" stop-color="var(--ember)"/>
            <stop offset="1" stop-color="var(--smoke)"/>
          </linearGradient>
        </defs>
        <path class="swoosh-upper" fill="var(--orange)"
              d="M0,36 C210,18 430,120 512,392 C420,170 220,78 0,80 Z"/>
        <path class="hero-photo" role="img" aria-label="Photo of a firefighter spraying water on a burning house"
              fill="url(#fire-tone)"
              d="M0,114 C210,100 420,200 506,392 C440,500 310,566 212,560 C120,552 40,410 0,262 Z"/>
        <path class="swoosh-lower" fill="var(--orange)"
              d="M0,400 C80,556 180,618 262,616 C400,612 520,420 588,324 L588,362 C520,452 400,590 262,594 C170,596 70,520 0,428 Z"/>
      </svg>

      <div class="brand">
        <div class="brand-name">BIRCHWELL</div>
        <div class="brand-sub">BIRCHWELL GROUP CLAIMS SERVICES</div>
      </div>

      <h1 class="headline">When<br>It Happens</h1>
      <p class="perils">Accidents, Disasters, Fire, Flood, Wind, Property &amp; Liability</p>

      <div class="service-band">24/7 Claim Service | Fast Reporting | Premium Quality</div>

      <div class="web-address">birchwellgroup.com</div>
    </article>
  </div>
</body>
</html>
```